Graphics for Vorlani telehealth weight loss plans

Vorlani focuses on delivering medical weight-loss using prescription medicine and telehealth consults. Vorlani needs graphics for its ecommerce site for three weight loss plans. The plans are posted here with current graphics and descriptions of what is included with each plan. Please do not feel constrained by current graphics or styling.

- https://shop.vorlanicare.com/products/steady-horizon-plan
- https://shop.vorlanicare.com/products/amber-ridge-plan
- https://shop.vorlanicare.com/products/calm-harbor-plan

The graphics need to look good on mobile and desktop browsers.

```html
<!DOCTYPE html>
<html lang="en">
<head>
<meta charset="utf-8">
<title>Vorlani telehealth weight loss plans</title>
<link href="https://fonts.googleapis.com/css2?family=Montserrat:wght@300;400;500;600;700;800;900&display=swap" rel="stylesheet">
<style>
  :root{
    --ink-grey:#8a8a8a;
    --cream:#fcf5ea;
    --white:#ffffff;
  }
  *{box-sizing:border-box;margin:0;padding:0}
  html,body{width:1200px;height:633px;overflow:hidden;background:var(--white);font-family:"Montserrat",sans-serif}
  .sheet{position:relative;width:1200px;height:633px}

  .sheet-title{position:absolute;left:214px;top:27px;display:flex;align-items:center;gap:14px}
  .sheet-title .mark{width:46px;height:46px;border:1.5px solid var(--ink-grey)}
  .sheet-title h1{font-weight:400;font-size:41px;color:var(--ink-grey);letter-spacing:.3px;line-height:1}

  .plan{position:absolute;top:108px;width:365px;height:487px;overflow:hidden}
  .plan--horizon{left:41px;
    --hero:#f9f5ef;--title:#0a3d4c;--subtitle:#8dc63f;
    --band-a:#97c93d;--band-a-ink:#0b3f4f;--band-b:#033f4f;--band-b-ink:#9ccb3b;
    --goal:#5b4fa0;--goal-hi:#a3d03a;--deep:#0a4250;--stem:#97c93d;
    --icon:#5b4fa0;--online:#033f4f;--pay:#5b4fa0;
    --figure-a:#0d3e4c;--figure-b:#7f96c4;--bloom-a:#ffffff;--bloom-b:#f1a92a;
    --photo-a:#e8ddd2;--photo-b:#2b2b2b;}
  .plan--harbor{left:420px;
    --hero:#fdf4e6;--title:#0d4f75;--subtitle:#0d4f75;
    --band-a:#30a8e0;--band-a-ink:#0c4466;--band-b:#116888;--band-b-ink:#ffffff;
    --goal:#e8972d;--goal-hi:#ffffff;--deep:#136a88;--stem:#30a8e0;
    --icon:#ea8a1f;--online:#136a88;--pay:#30a8e0;
    --figure-a:#0d3e4c;--figure-b:#4ab3e6;--bloom-a:#ffffff;--bloom-b:#f0c070;
    --photo-a:#f0ddd0;--photo-b:#f4d4d2;}
  .plan--ridge{left:799px;
    --hero:#eaf4fb;--title:#28306b;--subtitle:#28306b;
    --band-a:#f0bf5d;--band-a-ink:#283070;--band-b:#ee4b4b;--band-b-ink:#ffffff;
    --goal:#44579a;--goal-hi:#f5c04d;--deep:#136a88;--stem:#f0bf5d;
    --icon:#3d4f9c;--online:#ee5640;--pay:#ee4b3f;
    --figure-a:#ef6a45;--figure-b:#e29a78;--bloom-a:#ffffff;--bloom-b:#ee4b3f;
    --photo-a:#eedfd4;--photo-b:#6ea990;}

  .block{position:absolute}
  .hero{left:0;top:0;width:365px;height:170px;background:var(--hero)}
  .brand{position:absolute;left:15px;top:11px;display:flex;align-items:center;gap:4px;font-weight:500;font-size:11px;color:#111}
  .brand .mark{width:10px;height:10px;border:1px solid #111}
  .plan-name{position:absolute;left:14px;top:40px;line-height:34px;font-size:33px;color:var(--subtitle);font-weight:600}
  .plan-name strong{display:block;font-weight:900;color:var(--title)}
  .plan-name span{display:block}
  .photo{position:absolute;right:18px;top:4px;width:86px;height:166px;border-radius:43px 43px 0 0;
    background:linear-gradient(180deg,var(--photo-a) 0%,var(--photo-a) 45%,var(--photo-b) 100%)}

  .band-a{left:0;top:170px;width:204px;height:48px;background:var(--band-a);color:var(--band-a-ink);
    padding:10px 0 0 12px;font-weight:700;font-size:12.5px;line-height:15px}
  .plan--harbor .band-a{font-size:12px}
  .plan--harbor .band-a .lead{font-weight:400}
  .band-b{left:204px;top:170px;width:161px;height:48px;background:var(--band-b);color:var(--band-b-ink);
    display:flex;align-items:center;justify-content:center;font-weight:800;font-size:10.5px}

  .goal{left:0;top:218px;width:365px;height:92px;background:var(--goal)}
  .goal-text{position:absolute;left:177px;top:244px;z-index:3;color:var(--white);
    font-size:13.4px;font-weight:500;line-height:14px;white-space:nowrap}
  .goal-text b{font-weight:800;color:var(--goal-hi)}
  .shield{position:absolute;left:22px;top:232px;width:26px;height:28px;z-index:2}

  .deep{left:0;top:310px;width:178px;height:88px;background:var(--deep)}
  .figure{left:26px;top:214px;width:136px;height:184px;border-radius:68px 68px 10px 10px;
    background:linear-gradient(180deg,var(--figure-a) 0%,var(--figure-a) 45%,var(--figure-b) 100%)}

  .stem{left:178px;top:310px;width:91px;height:177px;background:var(--stem)}
  .bloom{left:190px;top:324px;width:70px;height:163px;border-radius:35px 35px 8px 8px;
    background:linear-gradient(180deg,var(--bloom-a) 0%,var(--bloom-b) 35%,#f6c9ad 80%)}

  .med{left:269px;top:310px;width:96px;height:88px;background:var(--cream);text-align:center;color:var(--icon)}
  .med svg{display:block;margin:16px auto 0;width:54px;height:46px}
  .med .label{font-size:6.5px;font-weight:700;margin-top:3px;letter-spacing:-.2px}
  .med .dose{font-size:6px;font-weight:300;color:#777}

  .pay{left:0;top:398px;width:178px;height:89px;background:var(--cream);padding:28px 0 0 30px}
  .pay .term{font-size:13px;font-weight:400;color:#555;line-height:14px}
  .pay .go{font-size:17px;font-weight:800;color:var(--pay);line-height:18px;letter-spacing:-.3px}

  .online{left:269px;top:398px;width:96px;height:89px;background:var(--online);color:var(--white);text-align:center;padding-top:30px}
  .online .pct{font-size:17px;font-weight:700;line-height:15px}
  .online .word{font-size:13px;font-weight:400;letter-spacing:.5px;line-height:14px}
  .online .note{font-size:5.8px;font-weight:300;margin-top:3px;opacity:.85}
</style>
</head>
<body>
<main class="sheet">
  <header class="sheet-title">
    <div class="mark"></div>
    <h1>Vorlani telehealth weight loss plans</h1>
  </header>

  <article class="plan plan--horizon">
    <div class="block hero">
      <div class="brand"><span class="mark"></span>Vorlani</div>
      <h2 class="plan-name"><strong>Steady</strong><span>Horizon</span><span>Plan</span></h2>
      <div class="photo" role="img" aria-label="Photo of a fit woman in black sportswear measuring her waist with a tape"></div>
    </div>
    <div class="block band-a">Physical Consultation<br>Phentermine Program</div>
    <div class="block band-b">Expert nutrition consult</div>
    <div class="block goal"></div>
    <div class="block deep"></div>
    <div class="block figure" role="img" aria-label="Illustration of a woman hugging a heart to her chest"></div>
    <p class="goal-text">Custom crafted diet plan<br>to <b>Achieve Your Goals</b></p>
    <svg class="shield" viewBox="0 0 26 28" aria-hidden="true"><path d="M13 1 L24 5 V13 C24 20 19 25 13 27 C7 25 2 20 2 13 V5 Z" fill="none" stroke="#fff" stroke-width="2.2"/><path d="M13 8v10M8 13h10" stroke="#fff" stroke-width="3"/></svg>
    <div class="block stem"></div>
    <div class="block bloom" role="img" aria-label="Illustration of a hand holding daisies"></div>
    <div class="block med">
      <svg viewBox="0 0 54 46" aria-hidden="true"><path d="M27 44 C10 32 2 24 2 14 C2 6 8 1 15 1 C20 1 24 4 27 8 C30 4 34 1 39 1 C46 1 52 6 52 14 C52 24 44 32 27 44 Z" fill="var(--icon)"/><rect x="17" y="17" width="16" height="8" rx="4" transform="rotate(-40 25 21)" fill="#fff"/><circle cx="35" cy="18" r="5" fill="#fff"/></svg>
      <div class="label">Real Phentermine</div>
      <div class="dose">(37.5mg / pill)</div>
    </div>
    <div class="block pay"><div class="term">Month-to-month</div><div class="go">Pay as you go</div></div>
    <div class="block online"><div class="pct">100%</div><div class="word">ONLINE</div><div class="note">No need to visit the office.</div></div>
  </article>

  <article class="plan plan--harbor">
    <div class="block hero">
      <div class="brand"><span class="mark"></span>Vorlani</div>
      <h2 class="plan-name"><strong>Calm</strong><span>Harbor</span><span>Plan</span></h2>
      <div class="photo" role="img" aria-label="Photo of a smiling woman in a pink sports top pointing at the plan name"></div>
    </div>
    <div class="block band-a"><span class="lead">Nutrition coaching to improve</span><br>Your health and vitality</div>
    <div class="block band-b">Expert nutrition consult</div>
    <div class="block goal"></div>
    <div class="block deep"></div>
    <div class="block figure" role="img" aria-label="Illustration of a woman hugging a heart to her chest"></div>
    <p class="goal-text">Custom crafted diet plan<br>to <b>Achieve Your Goals</b></p>
    <svg class="shield" viewBox="0 0 26 28" aria-hidden="true"><path d="M13 1 L24 5 V13 C24 20 19 25 13 27 C7 25 2 20 2 13 V5 Z" fill="none" stroke="#fff" stroke-width="2.2"/><path d="M13 8v10M8 13h10" stroke="#fff" stroke-width="3"/></svg>
    <div class="block stem"></div>
    <div class="block bloom" role="img" aria-label="Illustration of a hand holding daisies"></div>
    <div class="block med">
      <svg viewBox="0 0 54 46" style="margin-top:22px" aria-hidden="true"><path d="M27 44 C10 32 2 24 2 14 C2 6 8 1 15 1 C20 1 24 4 27 8 C30 4 34 1 39 1 C46 1 52 6 52 14 C52 24 44 32 27 44 Z" fill="var(--icon)"/><path d="M9 22 H20 L23 16 L27 29 L31 19 L33 22 H45" fill="none" stroke="#fff" stroke-width="1.4"/></svg>
    </div>
    <div class="block pay"><div class="term">Month-to-month</div><div class="go">Pay as you go</div></div>
    <div class="block online"><div class="pct">100%</div><div class="word">ONLINE</div><div class="note">No need to visit the office.</div></div>
  </article>

  <article class="plan plan--ridge">
    <div class="block hero">
      <div class="brand"><span class="mark"></span>Vorlani</div>
      <h2 class="plan-name"><strong>Amber</strong><span>Ridge</span><span>Plan</span></h2>
      <div class="photo" role="img" aria-label="Photo of a cheerful woman in a green sports top with fists raised"></div>
    </div>
    <div class="block band-a">Physical Consultation<br>Phentermine Program</div>
    <div class="block band-b">Medical consultation</div>
    <div class="block goal"></div>
    <div class="block deep"></div>
    <div class="block figure" role="img" aria-label="Illustration of a woman hugging a heart to her chest"></div>
    <p class="goal-text">Custom crafted diet plan<br>to <b>Achieve Your Goals</b></p>
    <svg class="shield" viewBox="0 0 26 28" aria-hidden="true"><path d="M13 1 L24 5 V13 C24 20 19 25 13 27 C7 25 2 20 2 13 V5 Z" fill="none" stroke="#fff" stroke-width="2.2"/><path d="M13 8v10M8 13h10" stroke="#fff" stroke-width="3"/></svg>
    <div class="block stem"></div>
    <div class="block bloom" role="img" aria-label="Illustration of a hand holding daisies"></div>
    <div class="block med">
      <svg viewBox="0 0 54 46" aria-hidden="true"><path d="M27 44 C10 32 2 24 2 14 C2 6 8 1 15 1 C20 1 24 4 27 8 C30 4 34 1 39 1 C46 1 52 6 52 14 C52 24 44 32 27 44 Z" fill="var(--icon)"/><rect x="17" y="17" width="16" height="8" rx="4" transform="rotate(-40 25 21)" fill="#fff"/><circle cx="35" cy="18" r="5" fill="#fff"/></svg>
      <div class="label">Real Phentermine</div>
      <div class="dose">(37.5mg / pill)</div>
    </div>
    <div class="block pay"><div class="term">Month-to-month</div><div class="go">Pay as you go</div></div>
    <div class="block online"><div class="pct">100%</div><div class="word">ONLINE</div></div>
  </article>
</main>
</body>
</html>
```